Harbor Petroleum Business Cards

I would like to design some options for about 10 sets of double sided business cards for our team with a raised logo with a Silver glossy finished logo. We are a privately funded upstream Oil & Gas producer drilling vertical wells in Central Oklahoma with a long term production (ROI driven) strategy that we implement through an annual drilling program. We are focused on a shallow / vertical / long life / low decline strategy. We are based in downtown Tulsa Oklahoma. I have attached a sample business card and a picture of our hallway logo which we would like to replicate on the business cards.

Target Market(s)

SEC Accredited Investors and other Oil & Gas Operators

Industry/Entity Type

Upstream Oil & Gas

Contact Information for Business Card

You can see the sample photo attached, but email / website / address / direct phone / Cell Phone / Name / Title / Fax

Font styles to use
Other font styles liked:
• Felix Titling

Colors
0054AA
0677BA
7BADD7
CADEEF
E8F1F8

Requirements
Must have
• Glossy raised logo
Nice to have
• Possibly a new logo.
Should not have
• No Greens /

```html
<!DOCTYPE html>
<html lang="en">
<head>
<meta charset="utf-8">
<title>Harbor Petroleum Business Cards</title>
<link href="https://fonts.googleapis.com/css2?family=Cinzel:wght@400;600&display=swap" rel="stylesheet">
<style>
  :root{
    --blue:#0054AA;
    --blue-mid:#0677BA;
    --blue-light:#7BADD7;
    --blue-pale:#CADEEF;
    --ink:#1a1a1a;
    --paper:#f7f7f5;
    --backdrop:#c8c9cb;
    --silver:#d9dde2;
  }
  *{margin:0;padding:0;box-sizing:border-box}
  html,body{width:1200px;height:801px;overflow:hidden}
  body{background:var(--backdrop);font-family:"Cinzel",serif;position:relative}
  .card{position:absolute;width:525px;height:300px;top:250px;border-radius:3px;box-shadow:0 14px 30px rgba(0,0,0,.22)}
  .card-front{left:50px;background:var(--paper);border-bottom:3px solid var(--blue)}
  .card-back{left:625px;background:var(--blue);display:flex;align-items:center;justify-content:center}
  .front-brand{position:absolute;left:28px;top:100px;width:160px;color:var(--blue);font-weight:400;font-size:30px;line-height:1.1;text-align:center}
  .divider{position:absolute;left:205px;top:40px;width:14px;height:220px}
  .details{position:absolute;left:236px;top:38px;color:var(--ink);font-size:11.5px;line-height:1.35}
  .name{color:var(--blue);font-size:19px;margin-bottom:4px;letter-spacing:.3px}
  .title{font-size:11.5px}
  .address{margin-top:10px}
  .contact{list-style:none;margin-top:10px;letter-spacing:1px}
  .contact li{display:flex;align-items:center;gap:7px;height:17px}
  .contact svg{width:11px;height:11px;fill:var(--blue);flex:none}
  .back-brand{color:var(--silver);font-weight:400;font-size:30px;letter-spacing:1px;text-align:center}
</style>
</head>
<body>
  <section class="card card-front" aria-label="Business card front">
    <div class="front-brand">Harbor Petroleum</div>
    <svg class="divider" viewBox="0 0 14 220" aria-hidden="true">
      <rect x="0" y="0" width="4" height="220" fill="var(--blue)"/>
      <rect x="6" y="0" width="3" height="220" fill="var(--blue-mid)"/>
      <rect x="11" y="0" width="3" height="220" fill="var(--blue-light)"/>
    </svg>
    <div class="details">
      <div class="name">Dalton J. Whitcomb, CPL</div>
      <div class="title">Executive Vice President</div>
      <div class="title">Land, Legal &amp; Business Development</div>
      <div class="address">42 East 9th Street<br>Suite 800<br>Tulsa, OK 74103</div>
      <ul class="contact">
        <li><svg viewBox="0 0 12 12"><path d="M2.5 0.5l2 2.2-1 1.3c.7 1.6 2 2.9 3.5 3.6l1.3-1 2.2 2-1.2 2.4C5 10.6 1.4 7 .4 1.6z"/></svg>539-555-0142</li>
        <li><svg viewBox="0 0 12 12"><path d="M3 0h6v12H3zM4 1.5v8h4v-8zM5.5 10.3h1v1h-1z" fill-rule="evenodd"/></svg>918-555-0187</li>
        <li><svg viewBox="0 0 12 12"><path d="M3 0h5v3H3zM1 3.5h10V12H1zM3 5v1.3h6V5zM3 8h1.5v1.3H3zm2.3 0h1.5v1.3H5.3zm2.3 0H9v1.3H7.6z" fill-rule="evenodd"/></svg>918-555-0163</li>
        <li><svg viewBox="0 0 12 12"><path d="M0 2h12v8H0zM1 3l5 3.8L11 3v-.2H1z" fill-rule="evenodd"/></svg>DJW@HPTULSA.COM</li>
        <li><svg viewBox="0 0 12 12"><circle cx="6" cy="6" r="5.5"/><path d="M.5 6h11M6 .5v11M2 3h8M2 9h8" stroke="var(--paper)" stroke-width=".8" fill="none"/></svg>WWW.HARBORPETROLEUMLLC.COM</li>
      </ul>
    </div>
  </section>

  <section class="card card-back" aria-label="Business card back">
    <div class="back-brand">Harbor Petroleum, LLC</div>
  </section>
</body>
</html>
```